Commercial Property Management Company needs business card design

We need an elegant business card design for our commercial property management company based in Hampton Falls, New Hampshire. We manage large retail shopping centers. These cards will be going out to current clients, retailers and to contractors.
I am the sole member of the company, so I'm not sure if I need to have a title with my name or not.

Industry/Entity Type

Property Management

Contact Information for Business Card

Colin R. Mabry
4 Pellow Lane
Ashby Falls, NH 03899
Cell: (603) 555-0142
Fax: (603) 555-0187
Email: colin@tovrenmanagementllc.com

```html
<!DOCTYPE html>
<html lang="en">
<head>
<meta charset="utf-8">
<title>Tovren Management, LLC — Business Card</title>
<link href="https://fonts.googleapis.com/css2?family=Arimo:wght@400;700&family=Cinzel:wght@400&display=swap" rel="stylesheet">
<style>
  :root {
    --backdrop: #ececec;
    --card: #ffffff;
    --ink: #2b2b2b;
    --ink-soft: #555555;
    --red: #c0272d;
    --orange: #e8571e;
    --amber: #f3a51b;
    --yellow: #f7d117;
  }
  * { box-sizing: border-box; margin: 0; padding: 0; }
  html, body {
    width: 1200px; height: 957px; overflow: hidden;
    background: var(--backdrop);
    font-family: "Arimo", Arial, sans-serif;
    color: var(--ink);
  }
  .sheet {
    width: 1200px; height: 957px;
    display: flex; flex-direction: column; align-items: center; justify-content: center;
    gap: 64px;
  }
  .card {
    position: relative;
    width: 595px; height: 340px;
    background: var(--card);
    box-shadow: 0 6px 20px rgba(0,0,0,0.10);
    overflow: hidden;
  }

  /* Front */
  .brand {
    position: absolute; inset: 0;
    display: flex; flex-direction: column; align-items: center; justify-content: center;
  }
  .brand-mark {
    width: 58px; height: 58px; border-radius: 50%;
    background: var(--red);
    margin-bottom: 14px;
  }
  .brand-name {
    font-family: "Cinzel", "Times New Roman", serif;
    font-weight: 400;
    font-size: 30px;
    letter-spacing: 0.5px;
    color: var(--ink);
  }
  .brand-tagline {
    margin-top: 4px;
    font-size: 15px; font-weight: 700;
    color: var(--red);
    letter-spacing: 0.3px;
  }

  /* Back */
  .contact {
    position: absolute; left: 48px; top: 58px;
  }
  .person-name {
    font-size: 21px; font-weight: 400; letter-spacing: 0.6px;
    text-transform: uppercase; color: var(--ink);
  }
  .person-title {
    margin-top: 3px;
    font-size: 13px; color: var(--orange);
  }
  .details {
    list-style: none; margin-top: 24px;
    display: flex; flex-direction: column; gap: 6px;
  }
  .details li {
    display: flex; align-items: center; gap: 10px;
    font-size: 12.5px; color: var(--ink-soft);
  }
  .details svg { width: 13px; height: 13px; flex: none; }
  .address {
    position: absolute; left: 48px; bottom: 58px;
    font-size: 12.5px; color: var(--ink-soft);
  }
  .edge-band {
    position: absolute; left: 0; right: 0; bottom: 30px; height: 7px;
    background: linear-gradient(90deg, var(--red) 0%, var(--red) 72%, var(--orange) 82%, var(--amber) 90%, var(--yellow) 100%);
  }
</style>
</head>
<body>
<main class="sheet">

  <section class="card card-front" aria-label="Card front">
    <div class="brand">
      <div class="brand-mark"></div>
      <div class="brand-name">Tovren Management, LLC</div>
      <div class="brand-tagline">Commercial property management</div>
    </div>
  </section>

  <section class="card card-back" aria-label="Card back">
    <div class="contact">
      <h1 class="person-name">Colin R. Mabry</h1>
      <p class="person-title">President</p>
      <ul class="details">
        <li>
          <svg viewBox="0 0 14 14" aria-hidden="true"><rect width="14" height="14" rx="2" fill="var(--red)"/><path d="M4 3.5l1.6 0 .7 2-1 .8a5 5 0 0 0 2.4 2.4l.8-1 2 .7v1.6c-3.8.4-6.9-2.7-6.5-6.5z" fill="#fff"/></svg>
          (603) 555-0142
        </li>
        <li>
          <svg viewBox="0 0 14 14" aria-hidden="true"><rect width="14" height="14" rx="2" fill="var(--red)"/><rect x="3" y="5.5" width="8" height="5" fill="#fff"/><rect x="4.5" y="3" width="5" height="2.5" fill="#fff"/></svg>
          (603) 555-0187
        </li>
        <li>
          <svg viewBox="0 0 14 14" aria-hidden="true"><rect width="14" height="14" rx="2" fill="var(--red)"/><rect x="3" y="4" width="8" height="6" fill="#fff"/><path d="M3 4l4 3.2L11 4" stroke="var(--red)" stroke-width="1" fill="none"/></svg>
          colin@tovrenmanagementllc.com
        </li>
        <li>
          <svg viewBox="0 0 14 14" aria-hidden="true"><rect width="14" height="14" rx="2" fill="var(--red)"/><circle cx="7" cy="7" r="3.6" stroke="#fff" stroke-width="1.1" fill="none"/><path d="M3.4 7h7.2M7 3.4v7.2" stroke="#fff" stroke-width="0.9"/></svg>
          www.tovrenmanagementllc.com
        </li>
      </ul>
    </div>
    <p class="address">4 Pellow Lane, Ashby Falls, NH 03899</p>
    <div class="edge-band"></div>
  </section>

</main>
</body>
</html>
```